I need a newspaper ads that suits events / outings all over the world. refreshing feeling that suits my company logo.
Size of the ads is 6cm by 6cm a square
takenote
1) Joining up as members is free .
2) Places of interest tickets discount for members
3) Special events / outings host almost everyday
4) main point is everyone able to know each another
website : www.WandermoorHub.com
Target Market(s)
Targeting general age 18-40 . mainly singles
contents to put inside the ads
2) Local Places of interest tickets discount for members
4) Website : www.WandermoorHub.com
5) We also host photos contest
6) Meet the different faces of the world
7) Experience Sharing Gathering !
Industry/Entity Type
It Company
Requirements
Must have
- Refreshing feeling , and professional . will be uploading more pictures , kindly put some pictures combine into it to make people feel there is a lot activities can be involve when they join as member.

```html
<!DOCTYPE html>
<html lang="en">
<head>
<meta charset="utf-8">
<title>Wandermoor Events – The Gate to the New World</title>
<link rel="stylesheet" href="https://fonts.googleapis.com/css2?family=Poppins:wght@500;600;700&display=swap">
<style>
  :root {
    --header-dark: #17465f;
    --header-mid: #1f6f95;
    --header-light: #3cb4dc;
    --panel: #4a4a4a;
    --panel-text: #ffffff;
    --bar: #cfcfcf;
    --bar-text: #333333;
    --page: #ffffff;
    --photo-green: #6f8f52;
    --photo-leaf: #9db874;
    --photo-stone: #7d7a70;
    --photo-warm: #b89a7c;
  }
  * { margin: 0; padding: 0; box-sizing: border-box; }
  html, body {
    width: 1195px;
    height: 1200px;
    overflow: hidden;
    background: var(--page);
  }
  .ad {
    position: relative;
    width: 1195px;
    height: 1200px;
    background: var(--page);
    font-family: "Poppins", sans-serif;
  }
  .header {
    position: absolute;
    left: 0; top: 0;
    width: 1195px; height: 262px;
    background: linear-gradient(90deg, var(--header-dark) 0%, var(--header-mid) 45%, var(--header-light) 100%);
  }
  .brand {
    position: absolute;
    left: 30px; top: 40px;
    width: 290px;
    display: flex;
    flex-direction: column;
    align-items: center;
    gap: 16px;
  }
  .brand-mark {
    width: 96px; height: 96px;
    border-radius: 50%;
    background: #ffffff;
    opacity: 0.9;
  }
  .brand-name {
    color: #ffffff;
    font-weight: 600;
    font-size: 30px;
    line-height: 1.15;
    letter-spacing: 3px;
    text-align: center;
  }
  .headline {
    position: absolute;
    left: 340px; top: 38px;
    width: 830px;
    color: #ffffff;
    font-weight: 700;
    font-size: 78px;
    line-height: 88px;
    text-align: center;
    letter-spacing: 1px;
    text-shadow: 2px 3px 3px rgba(0,0,0,0.35);
  }
  .photo {
    position: absolute;
    left: 8px;
    width: 651px;
  }
  .photo-top {
    top: 267px; height: 460px;
    background: linear-gradient(180deg, #dfe7dc 0%, var(--photo-leaf) 28%, var(--photo-green) 60%, #5a6b4a 100%);
  }
  .photo-bottom {
    top: 727px; height: 463px;
    background: linear-gradient(180deg, var(--photo-stone) 0%, #8d8579 35%, var(--photo-warm) 70%, #6a6f7c 100%);
  }
  .features {
    position: absolute;
    left: 672px; top: 267px;
    width: 523px; height: 890px;
    background: var(--panel);
    padding: 48px 30px 0 45px;
    list-style: none;
  }
  .features li {
    color: var(--panel-text);
    font-weight: 600;
    font-size: 36px;
    line-height: 46px;
    margin-bottom: 34px;
  }
  .web-bar {
    position: absolute;
    left: 680px; top: 1157px;
    width: 515px; height: 43px;
    background: var(--bar);
    color: var(--bar-text);
    font-weight: 500;
    font-size: 27px;
    line-height: 43px;
    text-align: center;
  }
</style>
</head>
<body>
  <main class="ad">
    <header class="header">
      <div class="brand">
        <div class="brand-mark"></div>
        <div class="brand-name">WANDERMOOR<br>EVENTS</div>
      </div>
      <h1 class="headline">THE GATE TO THE<br>NEW WORLD</h1>
    </header>

    <div class="photo photo-top" role="img" aria-label="Group of young members stacking hands together in a green park"></div>
    <div class="photo photo-bottom" role="img" aria-label="Group of young members posing together in front of a news board at an attraction"></div>

    <ul class="features">
      <li>1. Joining up as members is free</li>
      <li>2. Local Places of interest tickets discount for members</li>
      <li>3. Special events / outings host almost everyday</li>
      <li>4. We also host photos contest</li>
      <li>5. Meet the different faces of the world</li>
      <li>6. Experience Sharing Gathering !</li>
    </ul>

    <div class="web-bar">www.WandermoorHub.com</div>
  </main>
</body>
</html>
```